E-commerce portal dedicated for selling books

We are looking for a design of a professional and official e-commerce web-site for a new company that is specialized in selling books (both books formats, printed and electronic), we’ll deal also with used-books where we plan to buy used books and re-sell them to other clients, or let the clients can sell their used-books directly to another client,
Web site must be very clear for users who like to brows the site contents or to buy a book, we will make the books available in discounted prices.
Customer should be able to perform the following actions in the site:
Search the book he/she is looking for easily
Get a brief description and details about the author, publisher, book content, browse the book’s content, browse first 20 pages ,
View similar or related books and a list of books that other users who bought this books also bought
Read and write reviews
Sign-up in the site
Complete the purchase process
Users can also sell or buy used-books from the site.
Look and feel:
The site’s look and feel is preferred to be clean, simple and balanced
Web site design is preferred to be simple with no strong or dark colors
User should feel comfort when looking at the home page because the design simplicity and comfortable colors
I liked the following sites’ look and feel:
http://www.qirtas.ae/
http://www.velmora.com/
http://www.tulvinghart.com/
Please be sure to include all common elements that are used in the e-commerce web sites like Search, online form(s), shopping cart / ordering, user log in/member, printer-friendly function, subscription to newsletter.....

```html
<!DOCTYPE html>
<html lang="en">
<head>
<meta charset="utf-8">
<title>Pagewell Books</title>
<link href="https://fonts.googleapis.com/css2?family=Open+Sans:wght@400;600;700&family=Lora:wght@400;700&display=swap" rel="stylesheet">
<style>
:root{
  --blue:#1e7fc8;
  --blue-dark:#15609c;
  --sale:#b5243f;
  --ink:#1a1a1a;
  --muted:#777;
  --line:#9a9a9a;
  --price-off:#c8102e;
  --footer-bg:#e9e9e9;
  --footer-dark:#2b2b2b;
  --c1:#6b2d8f;--c2:#1e7fc8;--c3:#9bc31c;--c4:#f0a020;--c5:#e23a3a;--c6:#a3238e;
}
*{box-sizing:border-box;margin:0;padding:0}
html,body{width:1200px;height:1000px;overflow:hidden;background:#fff}
body{font-family:"Open Sans",Arial,sans-serif;color:var(--ink);position:relative}
.abs{position:absolute}
.rainbow{background:linear-gradient(90deg,var(--c1) 0 17%,var(--c2) 17% 40%,var(--c3) 40% 58%,var(--c4) 58% 75%,var(--c5) 75% 88%,var(--c6) 88%)}

/* top bar */
.topbar{left:273px;top:0;width:654px;height:22px;background:linear-gradient(#3a9ae0,#1668ad);color:#fff;font-size:8px;font-weight:600}
.topbar__user{position:absolute;left:60px;top:5px;display:flex;gap:6px;align-items:center}
.topbar__user::after{content:"";position:absolute;left:-6px;bottom:-5px;width:62px;height:2px;background:var(--c5)}
.topbar__right{position:absolute;right:60px;top:5px;display:flex;gap:14px;align-items:center}
.social-dots{display:flex;gap:3px}
.social-dots span{width:8px;height:8px;border-radius:50%;background:#fff}

/* header */
.header{left:322px;top:22px;width:556px;height:56px;background:linear-gradient(#fff,#ececec)}
.logo{position:absolute;left:17px;top:6px;font-size:25px;font-weight:700;color:var(--blue);letter-spacing:1px}
.search{position:absolute;left:143px;top:10px;width:275px;height:20px;border:1px solid #aaa;border-radius:3px;background:#fff;display:flex;align-items:center;font-size:7px}
.search__cat{width:76px;height:100%;border-right:1px solid #bbb;display:flex;align-items:center;gap:5px;padding-left:5px;background:#f1f1f1}
.search__input{padding-left:6px;color:#999;font-style:italic}
.go{position:absolute;left:412px;top:7px;width:26px;height:26px;border-radius:50%;background:radial-gradient(circle at 40% 35%,#4fb0ee,#1560a6);border:2px solid #fff;box-shadow:0 1px 3px #555;color:#fff;font-size:8px;font-weight:700;display:grid;place-items:center}
.add-cart{position:absolute;left:461px;top:9px;width:84px;height:20px;border-radius:10px;background:linear-gradient(#3ea4ea,#1667ad);color:#fff;font-size:7px;font-weight:700;display:flex;align-items:center;gap:6px;padding-left:6px}
.header__links{position:absolute;left:143px;top:38px;display:flex;gap:12px;font-size:7px;color:#444;align-items:center}
.header__links .hl{display:flex;gap:4px;align-items:center}
.header__links .how{color:var(--price-off)}

/* sidebar */
.shop{left:333px;top:84px;font-size:19px;font-weight:700;color:var(--blue)}
.shop-rule{left:333px;top:106px;width:104px;height:2px}
.shop-sub{left:333px;top:110px;font-size:9.5px;color:var(--blue);letter-spacing:.5px}
.categories{left:335px;top:135px;width:102px;list-style:none;font-size:6.3px}
.categories li{height:13.1px;display:flex;justify-content:space-between}
.categories li b{font-size:8px;line-height:6px}

/* hero */
.hero{left:451px;top:90px;width:298px;height:161px;border:1px solid #bbb;background:#fff;overflow:hidden}
.hero__art{position:absolute;left:20px;top:8px;width:250px;height:132px;background:linear-gradient(110deg,#e05a3a 0%,#f2c23c 25%,#4a8c7c 50%,#2b7a86 65%,#c9a14a 100%);opacity:.85}
.hero__title{position:absolute;left:142px;top:10px;width:150px;font-size:9.5px;font-weight:700;line-height:13px;background:#fff;padding-left:2px}
.hero__strip{position:absolute;left:0;bottom:0;width:100%;height:24px;background:linear-gradient(#3a98de,#1d6fb6);color:#fff;font-family:Lora,serif;font-style:italic;font-weight:700;font-size:11.5px;display:flex;align-items:center;justify-content:center}
.arrow-btn{position:absolute;width:23px;height:34px;background:var(--blue);border-radius:17px;display:grid;place-items:center;top:56px}
.sale{left:749px;top:90px;width:118px;height:161px;background:var(--sale);color:#fff;font-family:Lora,serif;text-align:center}
.sale__up{margin-top:18px;font-size:16px}
.sale__pct{font-size:13px;margin-top:2px}
.sale__word{font-size:30px;line-height:30px}
.sale__cta{font-size:8.5px;line-height:15px;margin-top:4px}
.sale__dots{position:absolute;left:50px;bottom:8px;display:flex;gap:3px}
.sale__dots span{width:4px;height:4px;border-radius:50%;background:#fff}

/* partners */
.partners-label{left:451px;top:262px;width:416px;text-align:center;font-size:7px}
.partners-label span{background:#fff;padding:0 6px;position:relative}
.partners-label::before{content:"";position:absolute;left:0;right:0;top:6px;height:1px;background:#aaa}
.partners{left:472px;top:273px;width:376px;display:flex;justify-content:space-between}
.partner{width:32px;height:32px;border-radius:50%;background:#cfcfcf}
.partner.sq{border-radius:3px;width:50px;height:20px;margin-top:6px;background:#555}
.partners-rule{left:451px;top:313px;width:416px;height:1px;background:#aaa}

/* sections */
.section-title{left:333px;font-size:11.5px;font-weight:400}
.view-all{left:820px;width:47px;text-align:right;font-size:6.5px;font-weight:700}
.section-rule{left:333px;width:534px;height:2px}
.card{position:absolute;width:98px;height:153px;border:1px solid #999;background:#fff}
.card--hover{box-shadow:0 0 6px rgba(0,0,0,.45)}
.card__cover{position:absolute;left:19px;top:6px;width:58px;height:86px;border:3px solid #888;background:var(--tone)}
.card__title{position:absolute;top:97px;width:100%;text-align:center;font-size:6.2px;font-weight:600}
.card__price{position:absolute;top:118px;left:5px;right:3px;display:flex;font-size:6.2px;gap:6px}
.card__price s{color:var(--muted)}
.card__price b{font-weight:700}
.card__price em{margin-left:auto;font-style:normal;color:var(--price-off)}
.card__cod{position:absolute;bottom:0;left:0;right:0;height:16px;border-top:1px solid #999;display:flex;align-items:center;gap:5px;padding-left:6px;font-size:5.6px;font-weight:700}
.ribbon{position:absolute;left:0;top:0;width:46px;height:46px;overflow:hidden}
.ribbon::before{content:"";position:absolute;left:-16px;top:12px;width:80px;height:10px;background:var(--blue);transform:rotate(-45deg)}

/* mini rows */
.mini-title{font-size:9.5px;top:707px}
.mini-rule{top:720px;height:2px}
.thumb{position:absolute;top:733px;width:54px;height:55px;border:1px solid #aaa;background:#fff}
.thumb i{position:absolute;left:9px;top:3px;width:36px;height:48px;background:var(--tone)}
.chev{position:absolute;top:752px}

/* footer */
.footer{left:322px;top:815px;width:556px;height:144px;background:var(--footer-bg);box-shadow:0 1px 4px rgba(0,0,0,.35)}
.footer__rule{position:absolute;left:0;top:0;width:100%;height:2px}
.fcol{position:absolute;top:17px;font-size:6px;color:#555}
.fcol h4{font-size:7px;font-weight:700;color:#333;margin-bottom:7px;letter-spacing:.3px}
.fcol li{list-style:none;height:14.2px}
.contact li{display:flex;gap:6px;height:auto;margin-bottom:4px;line-height:14px}
.contact .mail{color:var(--blue-dark);font-weight:700}
.contact .ico{width:10px;flex:none}
.fsocial{display:flex;gap:9px;margin-top:8px;margin-left:-2px}
.fsocial span{width:14px;height:14px;border-radius:2px;background:var(--blue)}
.fsocial span:last-child{background:var(--sale)}
.footer-bar{left:322px;top:959px;width:556px;height:35px;background:var(--footer-dark);color:#ddd;font-size:5.5px;display:flex;justify-content:space-between;align-items:center;padding:0 16px;box-shadow:0 1px 4px rgba(0,0,0,.35)}
.to-top{left:890px;top:947px;width:28px;height:28px;border-radius:50%;background:#111;display:grid;place-items:center}
</style>
</head>
<body>

<div class="abs topbar">
  <div class="topbar__user">
    <svg width="10" height="10" viewBox="0 0 10 10"><circle cx="5" cy="3" r="2.4" fill="#fff"/><path d="M0 10c0-3 2-4.5 5-4.5S10 7 10 10z" fill="#fff"/></svg>
    Hi, Me!
  </div>
  <div class="topbar__right">
    <span>▭ Help</span>
    <span>♡ wish list ▾</span>
    <span class="social-dots"><span></span><span></span><span></span><span></span></span>
  </div>
</div>

<header class="abs header">
  <div class="logo">LOGO</div>
  <div class="search">
    <div class="search__cat">
      <svg width="7" height="7" viewBox="0 0 10 10"><circle cx="4" cy="4" r="3" fill="none" stroke="#555" stroke-width="1.5"/><path d="M6 6l3 3" stroke="#555" stroke-width="1.5"/></svg>
      All Categories ▾
    </div>
    <div class="search__input">Search Over 30 Million foods</div>
  </div>
  <div class="go">GO</div>
  <div class="add-cart">
    <svg width="14" height="12" viewBox="0 0 14 12"><path d="M1 6l12-5-3 10-3-3-3 2z" fill="#fff"/></svg>
    ADD TO CART
  </div>
  <div class="header__links">
    <span class="hl how"><svg width="12" height="10" viewBox="0 0 12 10"><path d="M0 1h2l2 6h6l2-5H3" fill="none" stroke="#555"/><circle cx="5" cy="9" r="1" fill="#555"/><circle cx="9" cy="9" r="1" fill="#555"/></svg>How to shop?</span>
    <span class="hl"><svg width="7" height="10" viewBox="0 0 7 10"><path d="M3.5 0a3.5 3.5 0 0 0-3.5 3.5C0 6 3.5 10 3.5 10S7 6 7 3.5A3.5 3.5 0 0 0 3.5 0z" fill="#666"/><circle cx="3.5" cy="3.5" r="1.3" fill="#fff"/></svg>Choose My Store</span>
    <span class="hl"><svg width="9" height="9" viewBox="0 0 9 9"><rect x=".5" y="1.5" width="8" height="7" fill="none" stroke="#999"/></svg>Weekly Ad</span>
    <span class="hl">Advanced Search</span>
  </div>
</header>

<div class="abs shop">SHOP</div>
<div class="abs shop-rule rainbow"></div>
<div class="abs shop-sub">by CATEGORY</div>
<ul class="abs categories">
  <li>Academic and Professional<b>»</b></li>
  <li>Biographies &amp; Autobiographies<b>»</b></li>
  <li>Investing and Management<b>»</b></li>
  <li>Coffee Table<b>»</b></li>
  <li>College Text &amp; Reference<b>»</b></li>
  <li>Comics &amp; Graphic Novels<b>»</b></li>
  <li>Computers &amp; Internet<b>»</b></li>
  <li>Entrance Exams Preparation<b>»</b></li>
  <li>Literature &amp; Fiction<b>»</b></li>
  <li>Science &amp; Technology<b>»</b></li>
  <li>Teens<b>»</b></li>
  <li>Travel<b>»</b></li>
  <li>Other....</li>
</ul>

<section class="abs hero">
  <div class="hero__art" role="img" aria-label="Stack of colourful books beside featured book covers"></div>
  <div class="hero__title">Lorem ipsum dolor sit amet consectetur adipisicing elit</div>
  <div class="arrow-btn" style="left:0;border-radius:0 17px 17px 0"><svg width="8" height="12" viewBox="0 0 8 12"><path d="M6 1L2 6l4 5" fill="none" stroke="#fff" stroke-width="1.6"/></svg></div>
  <div class="arrow-btn" style="left:275px;border-radius:17px 0 0 17px"><svg width="8" height="12" viewBox="0 0 8 12"><path d="M2 1l4 5-4 5" fill="none" stroke="#fff" stroke-width="1.6"/></svg></div>
  <div class="hero__strip">Lorem ipsum dolor sit amet consectetur</div>
</section>
<aside class="abs sale">
  <div class="sale__up">Up to</div>
  <div class="sale__pct">50% Off</div>
  <div class="sale__word">SALE</div>
  <div class="sale__cta">Click herw to view<br>our sale items</div>
  <div class="sale__dots"><span></span><span></span><span></span></div>
</aside>

<div class="abs partners-label"><span>Our Company</span></div>
<svg class="abs" style="left:450px;top:282px" width="10" height="16" viewBox="0 0 10 16"><path d="M8 1L2 8l6 7" fill="none" stroke="#777" stroke-width="1.5"/></svg>
<div class="abs partners">
  <span class="partner"></span><span class="partner"></span><span class="partner sq"></span><span class="partner"></span><span class="partner"></span><span class="partner"></span>
</div>
<svg class="abs" style="left:858px;top:282px" width="10" height="16" viewBox="0 0 10 16"><path d="M2 1l6 7-6 7" fill="none" stroke="#777" stroke-width="1.5"/></svg>
<div class="abs partners-rule"></div>

<!-- Top new releases -->
<h2 class="abs section-title" style="top:328px">Top New Releases in Books</h2>
<div class="abs view-all" style="top:333px">View all &gt;&gt;</div>
<div class="abs section-rule rainbow" style="top:345px"></div>

<div class="card" style="left:333px;top:354px"><div class="card__cover" style="--tone:#9aa4a8" role="img" aria-label="Book cover with an owl"></div><div class="card__title">Lorem ipsum dolor sit amet</div><div class="card__price"><s>$300</s><b>$280</b><em>10% Off</em></div><div class="card__cod"><svg width="10" height="8" viewBox="0 0 12 10"><path d="M0 1h2l2 6h6l2-5H3" fill="none" stroke="#222" stroke-width="1.4"/><circle cx="5" cy="9" r="1" fill="#222"/><circle cx="9" cy="9" r="1" fill="#222"/></svg>Cash on delivery available</div></div>
<div class="card" style="left:441px;top:354px"><div class="card__cover" style="--tone:#b49a6c" role="img" aria-label="Book cover with a crane"></div><div class="ribbon"></div><div class="card__title">Lorem ipsum dolor sit amet</div><div class="card__price"><s>$75</s><b>$280</b><em>10% Off</em></div><div class="card__cod"><svg width="10" height="8" viewBox="0 0 12 10"><path d="M0 1h2l2 6h6l2-5H3" fill="none" stroke="#222" stroke-width="1.4"/><circle cx="5" cy="9" r="1" fill="#222"/><circle cx="9" cy="9" r="1" fill="#222"/></svg>Cash on delivery available</div></div>
<div class="card card--hover" style="left:549px;top:354px"><div class="card__cover" style="--tone:#2f8a74" role="img" aria-label="Book cover with a butterfly"></div><div class="card__title">Lorem ipsum dolor sit amet</div><div class="card__price"><s>$300</s><b>$280</b><em>10% Off</em></div><div class="card__cod"><svg width="10" height="8" viewBox="0 0 12 10"><path d="M0 1h2l2 6h6l2-5H3" fill="none" stroke="#222" stroke-width="1.4"/><circle cx="5" cy="9" r="1" fill="#222"/><circle cx="9" cy="9" r="1" fill="#222"/></svg>Cash on delivery available</div></div>
<div class="card" style="left:657px;top:354px"><div class="card__cover" style="--tone:#d7d2b4" role="img" aria-label="Book cover with a bird on a branch"></div><div class="card__title">Lorem ipsum dolor sit amet</div><div class="card__price"><s>$300</s><b>$280</b><em>10% Off</em></div><div class="card__cod"><svg width="10" height="8" viewBox="0 0 12 10"><path d="M0 1h2l2 6h6l2-5H3" fill="none" stroke="#222" stroke-width="1.4"/><circle cx="5" cy="9" r="1" fill="#222"/><circle cx="9" cy="9" r="1" fill="#222"/></svg>Cash on delivery available</div></div>
<div class="card" style="left:770px;top:354px"><div class="card__cover" style="--tone:#c9c6b6" role="img" aria-label="Illustrated novel cover"></div><div class="card__title">Lorem ipsum dolor sit amet</div><div class="card__price"><s>$300</s><s>$280</s><em>10% Off</em></div><div class="card__cod"><svg width="10" height="8" viewBox="0 0 12 10"><path d="M0 1h2l2 6h6l2-5H3" fill="none" stroke="#222" stroke-width="1.4"/><circle cx="5" cy="9" r="1" fill="#222"/><circle cx="9" cy="9" r="1" fill="#222"/></svg>Cash on delivery available</div></div>

<!-- Bestselling -->
<h2 class="abs section-title" style="top:515px">Bestselling Books at pagewell.com</h2>
<div class="abs view-all" style="top:521px">View all &gt;&gt;</div>
<div class="abs" style="left:333px;top:532px;width:534px;height:1px;background:#666"></div>

<div class="card" style="left:333px;top:542px"><div class="card__cover" style="--tone:#b8a98a" role="img" aria-label="Classic drama book cover"></div><div class="card__title">Lorem ipsum dolor sit amet</div><div class="card__price"><s>$300</s><b>$280</b><em>10% Off</em></div><div class="card__cod"><svg width="10" height="8" viewBox="0 0 12 10"><path d="M0 1h2l2 6h6l2-5H3" fill="none" stroke="#222" stroke-width="1.4"/><circle cx="5" cy="9" r="1" fill="#222"/><circle cx="9" cy="9" r="1" fill="#222"/></svg>Cash on delivery available</div></div>
<div class="card" style="left:441px;top:542px"><div class="card__cover" style="--tone:#e0a83a" role="img" aria-label="Travel book cover with a monument"></div><div class="ribbon"></div><div class="card__title">Lorem ipsum dolor sit amet</div><div class="card__price"><s>$75</s><b>$280</b><em>10% Off</em></div><div class="card__cod"><svg width="10" height="8" viewBox="0 0 12 10"><path d="M0 1h2l2 6h6l2-5H3" fill="none" stroke="#222" stroke-width="1.4"/><circle cx="5" cy="9" r="1" fill="#222"/><circle cx="9" cy="9" r="1" fill="#222"/></svg>Cash on delivery available</div></div>
<div class="card" style="left:549px;top:542px"><div class="card__cover" style="--tone:#5a2a22" role="img" aria-label="Dark history book cover"></div><div class="card__title">Lorem ipsum dolor sit amet</div><div class="card__price"><s>$300</s><b>$280</b><em>10% Off</em></div><div class="card__cod"><svg width="10" height="8" viewBox="0 0 12 10"><path d="M0 1h2l2 6h6l2-5H3" fill="none" stroke="#222" stroke-width="1.4"/><circle cx="5" cy="9" r="1" fill="#222"/><circle cx="9" cy="9" r="1" fill="#222"/></svg>Cash on delivery available</div></div>
<div class="card" style="left:657px;top:542px"><div class="card__cover" style="--tone:#c98a4a" role="img" aria-label="Epic poetry book cover"></div><div class="card__title">Lorem ipsum dolor sit amet</div><div class="card__price"><s>$300</s><s>$280</s><em>10% Off</em></div><div class="card__cod"><svg width="10" height="8" viewBox="0 0 12 10"><path d="M0 1h2l2 6h6l2-5H3" fill="none" stroke="#222" stroke-width="1.4"/><circle cx="5" cy="9" r="1" fill="#222"/><circle cx="9" cy="9" r="1" fill="#222"/></svg>Cash on delivery available</div></div>
<div class="card" style="left:770px;top:542px"><div class="card__cover" style="--tone:#3a2a22" role="img" aria-label="Dark war novel cover"></div><div class="card__title">Lorem ipsum dolor sit amet</div><div class="card__price"><s>$300</s><s>$280</s><em>10% Off</em></div><div class="card__cod"><svg width="10" height="8" viewBox="0 0 12 10"><path d="M0 1h2l2 6h6l2-5H3" fill="none" stroke="#222" stroke-width="1.4"/><circle cx="5" cy="9" r="1" fill="#222"/><circle cx="9" cy="9" r="1" fill="#222"/></svg>Cash on delivery available</div></div>

<!-- Recently viewed / Just for you -->
<div class="abs mini-title" style="left:363px">RECENTLY VIEWED</div>
<div class="abs mini-title" style="left:643px">JUST FOR YOU</div>
<div class="abs mini-rule rainbow" style="left:333px;width:534px"></div>

<svg class="chev" style="left:332px" width="10" height="16" viewBox="0 0 10 16"><path d="M8 1L2 8l6 7" fill="none" stroke="#777" stroke-width="1.5"/></svg>
<div class="thumb" style="left:363px"><i style="--tone:#7a4a2a" role="img" aria-label="Book cover"></i></div>
<div class="thumb" style="left:433px"><i style="--tone:#6f7058" role="img" aria-label="Book cover"></i></div>
<div class="thumb" style="left:502px"><i style="--tone:#2a2622" role="img" aria-label="Science book cover"></i></div>
<svg class="chev" style="left:574px" width="10" height="16" viewBox="0 0 10 16"><path d="M2 1l6 7-6 7" fill="none" stroke="#777" stroke-width="1.5"/></svg>
<div class="abs" style="left:598px;top:733px;width:1px;height:55px;background:#999"></div>
<svg class="chev" style="left:612px" width="10" height="16" viewBox="0 0 10 16"><path d="M8 1L2 8l6 7" fill="none" stroke="#777" stroke-width="1.5"/></svg>
<div class="thumb" style="left:644px"><i style="--tone:#b86a3a" role="img" aria-label="Animal book cover"></i></div>
<div class="thumb" style="left:713px"><i style="--tone:#4a4040" role="img" aria-label="Biography book cover"></i></div>
<div class="thumb" style="left:783px"><i style="--tone:#1d3a6a" role="img" aria-label="Physics book cover"></i></div>
<svg class="chev" style="left:856px" width="10" height="16" viewBox="0 0 10 16"><path d="M2 1l6 7-6 7" fill="none" stroke="#777" stroke-width="1.5"/></svg>

<footer class="abs footer">
  <div class="footer__rule rainbow"></div>
  <div class="fcol" style="left:20px"><h4>INFORMATION</h4><ul><li>&gt; About Store</li><li>&gt; Contact Us</li><li>&gt; Customer Assistance</li><li>&gt; Privacy Policy</li><li>&gt; Terms &amp; Condition</li><li>&gt; Worldwide Delivery</li></ul></div>
  <div class="fcol" style="left:153px"><h4>SHIPPING &amp; SUPPORT</h4><ul><li>&gt; International Shipping</li><li>&gt; Orders and Returns</li><li>&gt; Delivery Information</li><li>&gt; Secure Shopping</li></ul></div>
  <div class="fcol" style="left:291px"><h4>MY ACCOUNT</h4><ul><li>&gt; My Account</li><li>&gt; Order History</li><li>&gt; Manugactures</li><li>&gt; New Collection</li><li>&gt; Wish List</li><li>&gt; Newsletter</li></ul></div>
  <div class="fcol contact" style="left:415px;width:135px"><h4 style="margin-left:14px">CONTACT US</h4><ul>
    <li><svg class="ico" width="8" height="10" viewBox="0 0 7 10"><path d="M3.5 0a3.5 3.5 0 0 0-3.5 3.5C0 6 3.5 10 3.5 10S7 6 7 3.5A3.5 3.5 0 0 0 3.5 0z" fill="#333"/></svg><span>No 18 Linden Row 42/7 Harborview<br>City, HV Northland</span></li>
    <li><svg class="ico" width="9" height="7" viewBox="0 0 9 7"><rect width="9" height="7" fill="#333"/><path d="M0 0l4.5 4L9 0" stroke="#fff" fill="none"/></svg><span class="mail">hello@pagewell-mail.com<br>hello@pagewell-mail.com</span></li>
    <li><svg class="ico" width="9" height="8" viewBox="0 0 9 8"><path d="M0 2q4.5-3 9 0v1H7V2H2v1H0zM1 4h7v4H1z" fill="#333"/></svg><span class="mail">(+12) 05550199-314<br>(+12) 05550199-314</span></li>
  </ul>
  <div class="fsocial" style="margin-left:12px"><span></span><span></span><span></span><span></span></div></div>
</footer>
<div class="abs footer-bar"><span>Copy right 2013 pagewell.com All right reserved</span><span>Delivery &amp; Returns &nbsp;|&nbsp; Terms &amp; conditions &nbsp;|Site Map &nbsp;| &nbsp;About Us</span></div>
<div class="abs to-top"><svg width="14" height="10" viewBox="0 0 14 10"><path d="M2 8l5-5 5 5" fill="none" stroke="#fff" stroke-width="3"/></svg></div>

</body>
</html>
```